Linewire Trade Journal Adverts

We need an advertisement design for our company 'Ember Ridge' www.emberridge-example.com
Ember Ridge is a telecommunication business that develop three different service. Cloud, Voice and Connectivity.
We are wanting to put an advertisement into Linewire Trade and would like the design, design that reflects our current brand and captures individual attention.
This advertisement needs to look professional and eye catching.
3 different advertisements are needed and I would like them to all be different yet link together in design so they can be recognised as Ember Ridge.
I have attached our logo below, along with the three advertisements.
Target Market(s)
Direct Reseller customers
Industry/Entity Type
Telecommunications
Requirements
Must have
- My project must follow our current branding that is on our website

```html
<!DOCTYPE html>
<html lang="en">
<head>
<meta charset="utf-8">
<title>Ember Ridge – Linewire Trade advert options</title>
<link href="https://fonts.googleapis.com/css2?family=Ubuntu:wght@400;500;700&family=Open+Sans:wght@400;600;700&display=swap" rel="stylesheet">
<style>
  :root {
    --magenta: #e6067f;
    --charcoal: #3b3b3d;
    --slate: #6b6b6d;
    --board: #f2f2f2;
    --white: #ffffff;
    --ink: #2b2b2b;
    --plum: #5b2c83;
  }
  * { box-sizing: border-box; margin: 0; padding: 0; }
  html, body { width: 1200px; height: 887px; overflow: hidden; background: var(--board); }
  body { position: relative; font-family: "Ubuntu", sans-serif; }

  .option-label {
    position: absolute; top: 42px; width: 512px; text-align: center;
    font-family: "Open Sans", sans-serif; font-size: 27px; color: #111;
  }

  .advert {
    position: absolute; top: 106px; width: 512px; height: 725px;
    background: var(--white); overflow: hidden;
    box-shadow: 5px 6px 8px rgba(0,0,0,.35);
  }
  .advert--grey  { left: 58px;
    --hero-bg: linear-gradient(90deg, #8a8a8c 0%, #6c6c6e 55%, #5e5e60 100%);
    --strip: var(--magenta); --side: var(--magenta); --band: var(--charcoal); --footer: var(--magenta); }
  .advert--pink  { left: 636px;
    --hero-bg: linear-gradient(90deg, #f07ab4 0%, #ea2c8f 45%, #e6067f 100%);
    --strip: var(--slate); --side: var(--charcoal); --band: var(--magenta); --footer: var(--charcoal); }

  .hero { position: absolute; left: 0; top: 0; width: 512px; height: 182px; background: var(--hero-bg); }
  .hero__brand {
    position: absolute; left: 34px; top: 44px; width: 160px; font-size: 36px; font-weight: 700;
    line-height: 40px; color: rgba(255,255,255,.55);
  }
  .hero__title {
    position: absolute; left: 231px; top: 20px; color: var(--white);
    font-size: 26px; font-weight: 700; line-height: 27px; white-space: nowrap;
  }
  .hero__strip {
    position: absolute; left: 202px; top: 104px; right: 0; height: 65px;
    background: var(--strip); padding: 4px 0 0 29px;
  }
  .hero__strip li {
    list-style: none; color: var(--white); font-size: 16px; font-weight: 700; line-height: 19px;
    position: relative; padding-left: 14px; white-space: nowrap;
  }
  .hero__strip li::before {
    content: ""; position: absolute; left: 0; top: 6px; width: 7px; height: 7px;
    border-radius: 50%; background: var(--white);
  }

  .photo {
    position: absolute; left: 0; top: 182px; width: 512px; height: 205px;
    background:
      radial-gradient(ellipse at 70% 35%, rgba(210,235,250,.55), transparent 55%),
      linear-gradient(100deg, #1f2a3a 0%, #2b3c52 35%, #5d7f9e 65%, #8fb0c8 100%);
  }

  .pitch { position: absolute; left: 0; top: 387px; width: 512px; height: 170px; background: var(--white); }
  .pitch__side { position: absolute; right: 0; top: 0; width: 88px; height: 100%; background: var(--side); }
  .pitch__text {
    position: absolute; left: 35px; top: 12px; color: var(--ink);
    font-size: 29px; font-weight: 500; line-height: 29.5px; white-space: nowrap;
  }
  .pitch__text strong { font-weight: 700; }
  .pitch__text .accent { color: var(--magenta); font-weight: 700; font-size: 36px; }

  .band {
    position: absolute; left: 0; top: 557px; width: 512px; height: 49px; background: var(--band);
    color: var(--white); font-family: "Open Sans", sans-serif; font-weight: 700;
    font-size: 11.5px; line-height: 16px; text-align: center; padding-top: 8px; white-space: nowrap;
  }

  .partners { position: absolute; left: 0; top: 606px; width: 512px; height: 73px; background: var(--white); }
  .partners__grid {
    position: absolute; left: 22px; top: 10px; width: 270px;
    display: grid; grid-template-columns: repeat(4, 1fr); row-gap: 14px; column-gap: 4px;
  }
  .partners__name {
    font-size: 10px; font-weight: 700; color: #5a5a5c; text-align: center; line-height: 14px; white-space: nowrap;
  }
  .partners__cta {
    position: absolute; left: 308px; top: 16px; color: var(--plum);
    font-size: 12.5px; font-weight: 700; line-height: 12.5px; white-space: nowrap;
  }
  .partners__brand {
    position: absolute; left: 418px; top: 21px; display: flex; align-items: center; gap: 5px;
    color: var(--magenta); font-size: 15px; font-weight: 700; line-height: 15px; width: 90px;
  }
  .partners__brand .mark { flex: none; width: 12px; height: 12px; background: var(--magenta); }

  .footer {
    position: absolute; left: 0; top: 679px; width: 512px; height: 46px; background: var(--footer);
    color: var(--white); font-family: "Open Sans", sans-serif; font-size: 10px; line-height: 14px;
  }
  .footer__col { position: absolute; top: 9px; width: 248px; text-align: center; white-space: nowrap; }
  .footer__col--address { left: 0; }
  .footer__col--contact { left: 248px; width: 264px; }
  .footer__divider { position: absolute; left: 248px; top: 6px; width: 1px; height: 36px; background: var(--white); }
</style>
</head>
<body>

<div class="option-label" style="left:58px">Option-1</div>
<div class="option-label" style="left:636px">Option-2</div>

<article class="advert advert--grey">
  <header class="hero">
    <div class="hero__brand">Ember<br>Ridge</div>
    <h2 class="hero__title">Most channel<br>partners offer these<br>benefits as standard:</h2>
    <ul class="hero__strip">
      <li>Account management</li>
      <li>A secure portal</li>
      <li>An automated billing engine</li>
    </ul>
  </header>
  <div class="photo" role="img" aria-label="Photograph of a businessman in a suit and blue tie using a tablet against a blurred blue city-lights background"></div>
  <section class="pitch">
    <p class="pitch__text">But what about <span class="accent">£2m</span><br>additional revenue<br>in only <span class="accent">12 months?</span><br><strong>There’s nothing standard<br>about that...</strong></p>
    <div class="pitch__side"></div>
  </section>
  <div class="band">We’ll supercharge your business with secure cloud-first voice,<br>network and storage solutions that enable your clients – and you – to thrive.</div>
  <section class="partners">
    <div class="partners__grid">
      <span class="partners__name">Northvale</span><span class="partners__name">Keystack</span><span class="partners__name">Tallyline</span><span class="partners__name">Brightvault</span>
      <span class="partners__name">Corelink</span><span class="partners__name">Harbour Biz</span><span class="partners__name">Chatterbox</span><span class="partners__name">Vectorspan</span>
    </div>
    <p class="partners__cta">Talk to us<br>about your<br>partner potential</p>
    <div class="partners__brand"><span class="mark"></span><span>Ember Ridge</span></div>
  </section>
  <footer class="footer">
    <div class="footer__col footer__col--address">The Foundry, Millbrook Close,<br>Millbrook Business Park, Ashdale, AB1 2CD</div>
    <div class="footer__divider"></div>
    <div class="footer__col footer__col--contact">www.emberridge-example.com<br>T: 0300 555 0199 E: info@emberridge-example.com</div>
  </footer>
</article>

<article class="advert advert--pink">
  <header class="hero">
    <div class="hero__brand">Ember<br>Ridge</div>
    <h2 class="hero__title">Most channel<br>partners offer these<br>benefits as standard:</h2>
    <ul class="hero__strip">
      <li>Account management</li>
      <li>A secure portal</li>
      <li>An automated billing engine</li>
    </ul>
  </header>
  <div class="photo" role="img" aria-label="Photograph of a businessman in a suit and blue tie using a tablet against a blurred blue city-lights background"></div>
  <section class="pitch">
    <p class="pitch__text">But what about <span class="accent">£2m</span><br>additional revenue<br>in only <span class="accent">12 months?</span><br><strong>There’s nothing standard<br>about that...</strong></p>
    <div class="pitch__side"></div>
  </section>
  <div class="band">We’ll supercharge your business with secure cloud-first voice,<br>network and storage solutions that enable your clients – and you – to thrive.</div>
  <section class="partners">
    <div class="partners__grid">
      <span class="partners__name">Northvale</span><span class="partners__name">Keystack</span><span class="partners__name">Tallyline</span><span class="partners__name">Brightvault</span>
      <span class="partners__name">Corelink</span><span class="partners__name">Harbour Biz</span><span class="partners__name">Chatterbox</span><span class="partners__name">Vectorspan</span>
    </div>
    <p class="partners__cta">Talk to us<br>about your<br>partner potential</p>
    <div class="partners__brand"><span class="mark"></span><span>Ember Ridge</span></div>
  </section>
  <footer class="footer">
    <div class="footer__col footer__col--address">The Foundry, Millbrook Close,<br>Millbrook Business Park, Ashdale, AB1 2CD</div>
    <div class="footer__divider"></div>
    <div class="footer__col footer__col--contact">www.emberridge-example.com<br>T: 0300 555 0199 E: info@emberridge-example.com</div>
  </footer>
</article>

</body>
</html>
```